Business card for a plastic surgeon

i need a business card for a plastic surgeon. I have two adresses. The card should communicate safety, simmetry, beauty and with soft colors.
What i want in the card:
- my logo: Letters "R"and "T" (picture uploaded)
- my name: Rodrigo Tavernelli
- my registration: CRM 527 319
- my adresses and phone numbers (2):
- Av Dr Bento Arruda, 2730, sala 408 - Vila Olímpia | São Paulo/ SP - Phone: 11 4721-6350
- Al. Itaquera, 61, 3 andar - Alphaville | Barueri/ SP - Phone: 11 5038-2917

- my social network: site, facebook and instagram

Target Market(s)

people (95% girls and women) that want cosmetic procedures and plastic surgery

Industry/Entity Type

Business

Contact Information for Business Card

The card should communicate safety, simmetry, beauty and with soft colors.
Beige, brown, gray, rosy are some options. Color is free

Font styles to use
Serif

Requirements
Must have
• - my logo: Letters "R"and "T" (picture uploaded)
• - my name: Rodrigo Tavernelli
• - my registration: CRM 527 319
• - my adresses and phone numbers (2):
• - Av Dr Bento Arruda, 2730, sala 408 - Vila Olímpia | São Paulo/ SP - Phone: 11 4721-6350
• - Al. Itaquera, 61, 3 andar - Alphaville | Barueri/ SP - Phone: 11 5038-2917
• - my social network: site, facebook and instagram
Should not have
• other images (only my logo)

```html
<!DOCTYPE html>
<html lang="pt-BR">
<head>
<meta charset="utf-8">
<title>Dr. Rodrigo Tavernelli – Cartão de Visita</title>
<link rel="stylesheet" href="https://fonts.googleapis.com/css2?family=Cinzel:wght@400;500&family=Open+Sans:wght@400;600&display=swap">
<style>
  :root {
    --backdrop: #2b2b2b;
    --ink: #0a0a0a;
    --paper: #ffffff;
    --tan: #a08a74;
    --text-dark: #1c1c1c;
    --text-light: #f2f2f2;
  }
  * { box-sizing: border-box; margin: 0; padding: 0; }
  html, body {
    width: 1200px; height: 880px; overflow: hidden;
    background: var(--backdrop);
  }
  .canvas { position: relative; width: 1200px; height: 880px; }

  .card {
    position: absolute; width: 620px; height: 354px;
    border-radius: 18px; overflow: hidden;
    box-shadow: 0 12px 30px rgba(0,0,0,.45);
  }

  /* Front: black card */
  .card-front {
    left: 110px; top: 60px; background: var(--ink); color: var(--text-light);
    display: flex; flex-direction: column; align-items: center; justify-content: center;
    text-align: center;
  }
  .monogram {
    font-family: 'Cinzel', serif; font-weight: 400;
    letter-spacing: -4px; line-height: 1;
  }
  .card-front .monogram { font-size: 64px; color: var(--text-light); margin-bottom: 18px; }
  .doctor-name {
    font-family: 'Cinzel', serif; font-weight: 400; font-size: 29px;
    letter-spacing: 1px; line-height: 1.05;
  }
  .specialty {
    font-family: 'Cinzel', serif; font-size: 14px; letter-spacing: 7px;
    margin-top: 4px;
  }
  .website {
    font-family: 'Open Sans', sans-serif; font-size: 15px; margin-top: 26px;
  }
  .website .domain { color: var(--tan); }

  /* Back: contact card */
  .card-back { left: 470px; top: 466px; background: var(--paper); color: var(--text-dark); }
  .divider { position: absolute; inset: 0; }
  .card-back .monogram {
    position: absolute; left: 470px; top: 92px; font-size: 120px; color: var(--tan);
  }
  .contact-block { position: absolute; left: 36px; top: 52px; width: 370px; }
  .contact-block .doctor-name { font-size: 28px; }
  .contact-block .specialty { font-size: 13px; letter-spacing: 6px; }
  .person {
    font-family: 'Cinzel', serif; font-size: 20px; color: var(--tan);
    margin-top: 34px; line-height: 1;
  }
  .registration, .address, .phone {
    font-family: 'Open Sans', sans-serif; font-size: 13.5px; line-height: 1.4;
  }
  .address-group { margin-top: 14px; }
  .address-group + .address-group { margin-top: 12px; }
  .phone .label { color: var(--tan); font-weight: 600; }

  .social {
    position: absolute; right: 30px; bottom: 70px;
    display: flex; align-items: center; gap: 6px;
    font-family: 'Open Sans', sans-serif; font-size: 12px; color: var(--tan);
  }
  .social .square { width: 12px; height: 12px; background: var(--tan); }
</style>
</head>
<body>
<main class="canvas">

  <section class="card card-front" aria-label="Frente do cartão">
    <div class="monogram">RT</div>
    <h1 class="doctor-name">DR. RODRIGO TAVERNELLI</h1>
    <p class="specialty">CIRURGIÃO PLÁSTICO</p>
    <p class="website">www.<span class="domain">rtcirurgia</span>.com.br</p>
  </section>

  <section class="card card-back" aria-label="Verso do cartão">
    <svg class="divider" width="620" height="354" viewBox="0 0 620 354" aria-hidden="true">
      <path d="M396,0 C446,110 540,200 512,354 L620,354 L620,0 Z" fill="var(--tan)"/>
      <path d="M410,0 C460,110 554,200 526,354 L620,354 L620,0 Z" fill="var(--paper)"/>
      <path d="M424,0 C474,110 568,200 540,354 L620,354 L620,0 Z" fill="var(--ink)"/>
    </svg>
    <div class="monogram">RT</div>

    <div class="contact-block">
      <h2 class="doctor-name">DR. RODRIGO TAVERNELLI</h2>
      <p class="specialty">CIRURGIÃO PLÁSTICO</p>
      <p class="person">RODRIGO TAVERNELLI</p>
      <p class="registration">CRM 527 319</p>
      <div class="address-group">
        <p class="address">Av Dr Bento Arruda, 2730, sala 408<br>Vila Olímpia | São Paulo/ SP</p>
        <p class="phone"><span class="label">P:</span> 11 4721-6350</p>
      </div>
      <div class="address-group">
        <p class="address">Al. Itaquera, 61, 3 andar, Alphaville | Barueri/ SP</p>
        <p class="phone"><span class="label">P:</span> 11 5038-2917</p>
      </div>
    </div>

    <div class="social"><span class="square"></span>@rtcirurgia</div>
  </section>

</main>
</body>
</html>
```